web and logo design for insurance quote site

i want a quoteform site simimar to brimtallow.com i have a site up now @ kvbrimtallow.com, its functional but not attractive

Target Market(s)

people looking to get a home, auto or life insurance quote

Industry/Entity Type

Insurance

Number of Pages Required

1 page

Requirements
Must have
• great form that gathers all the information and emails the form to me
Nice to have
• nice eye catching art design thatI can have printed on business cards to send poeople to the site

```html
<!DOCTYPE html>
<html lang="en">
<head>
<meta charset="utf-8">
<title>KVBRIMTALLOW.com – Compare Insurance Quotes</title>
<link href="https://fonts.googleapis.com/css2?family=Questrial&family=Arimo:wght@400;700&family=Nunito:wght@900&display=swap" rel="stylesheet">
<style>
:root{
  --page:#878787;
  --panel:#6e6e6e;
  --panel-dark:#2c2c2c;
  --lime:#ccff00;
  --lime-deep:#8fc000;
  --text-light:#f0f0f0;
  --text-dark:#1c1c1c;
  --field:#ffffff;
}
*{box-sizing:border-box;margin:0;padding:0}
html,body{width:942px;height:1200px;overflow:hidden}
body{background:var(--page);font-family:"Questrial",sans-serif;color:var(--text-light);position:relative}
.abs{position:absolute}
.flag{left:18px;top:9px;width:26px;height:15px;background:linear-gradient(#b22 0 50%,#eee 50%);border:1px solid #555}
.login-prompt{left:427px;top:16px;font:11px "Arimo",sans-serif;color:#fff}
.login-prompt b{color:var(--lime);font-weight:400}
.login-label{font:11px "Arimo",sans-serif;color:#fff;text-align:right;width:90px}
.field{background:var(--field);border:1px solid #ccc;height:18px}
.pill{background:linear-gradient(#e4ff60,var(--lime) 45%,#9acc00);border-radius:12px;color:#222;font:12px "Arimo",sans-serif;text-align:center;line-height:22px;box-shadow:2px 3px 3px rgba(0,0,0,.45)}
.nav{left:17px;top:77px;font:11px "Arimo",sans-serif;color:#111}
.nav span{margin:0 5px}
.masthead{left:0;top:97px;width:865px;height:223px;background:linear-gradient(#111 0%,#555 30%,#c9c9c9 62%,#fff 80%);box-shadow:3px 3px 4px rgba(0,0,0,.5)}
.brand{left:14px;top:192px;font-size:53px;color:var(--text-dark);letter-spacing:-1px}
.tagline{left:12px;top:262px;font-size:18px;color:var(--text-dark)}
.call{right:103px;top:172px;text-align:right;font-family:"Nunito",sans-serif;color:var(--lime);line-height:1.05}
.call .now{font-size:32px}
.call .phone{font-size:35px}
.categories{left:0;top:331px;width:630px;height:98px;background:var(--panel-dark)}
.cat{position:absolute;top:5px;width:74px;height:70px}
.cat-label{position:absolute;top:80px;font:11px "Arimo",sans-serif;color:#fff;width:80px;text-align:center}
.register{left:634px;top:331px;width:228px;height:98px;background:var(--panel-dark);padding:10px 14px}
.register p{font:11px/1.3 "Arimo",sans-serif;color:#fff}
.register .cta{margin-top:12px;font-size:19px;color:var(--lime)}
.sidebar{left:0;top:441px;width:228px;height:387px;background:var(--panel)}
.bar{background:linear-gradient(90deg,#222,#3a3a3a);height:26px}
.sidebar .bar{font:11px/26px "Arimo",sans-serif;padding-left:8px;color:#fff}
.news{padding:8px 9px 0;font-size:11px;line-height:1.3}
.news .date{color:var(--lime);font-family:"Arimo",sans-serif}
.news .more{color:var(--lime);text-align:right;margin-top:2px}
.news-item{margin-bottom:16px}
.side-btn{width:136px;height:58px;background:linear-gradient(#e8ff70,var(--lime) 50%,#a8dd00);border-radius:6px;color:#222;font-size:21px;line-height:1.1;padding:4px 12px;box-shadow:3px 3px 3px rgba(0,0,0,.5)}
.main{left:233px;width:629px;background:var(--panel)}
.main .bar{height:26px;padding-left:28px;font-size:22px;line-height:30px}
.copy{padding:10px 16px;font-size:11px;line-height:1.3}
.copy b{color:var(--lime);font-weight:400}
.help .bar{color:var(--lime)}
.section-label{font-size:11px;color:#fff}
.form-label{font-size:10.5px;color:#fff;text-align:right}
.btn-caption{font-size:11px;color:#fff}
.footer{left:232px;top:1175px;font:11px "Arimo",sans-serif;color:#fff}
</style>
</head>
<body>

<div class="abs flag" role="img" aria-label="Country flag for language selection"></div>
<div class="abs login-prompt">To retrieve a quote &gt; <b>LOGIN &gt;&gt;</b></div>
<div class="abs login-label" style="left:576px;top:16px">Email Address:</div>
<div class="abs field" style="left:671px;top:8px;width:190px"></div>
<div class="abs login-label" style="left:576px;top:43px">Password:</div>
<div class="abs field" style="left:671px;top:37px;width:190px"></div>
<div class="abs pill" style="left:669px;top:61px;width:77px">LOGIN</div>
<div class="abs pill" style="left:760px;top:61px;width:92px">FORGOTTEN?</div>

<nav class="abs nav">Home<span>|</span>About Us<span>|</span>Contact Us<span>|</span>Sitemap<span>|</span>Legal Stuff<span>|</span>BOOKMARK</nav>

<header class="abs masthead"></header>
<div class="abs brand">KVBRIMTALLOW.com</div>
<div class="abs tagline">Compare Insurance Quotes,&nbsp; Get Insurance Quotes</div>
<div class="abs call"><div class="now">Call Now</div><div class="phone">(555) 014-2290</div></div>

<section class="abs categories">
  <div class="cat" style="left:37px;background:linear-gradient(135deg,#ddd,#8fbf20)" role="img" aria-label="Small green car for auto insurance"></div>
  <div class="cat-label" style="left:49px">AUTO</div>
  <div class="cat" style="left:157px;background:linear-gradient(135deg,#eee,#7a9a6a)" role="img" aria-label="Model house for home insurance"></div>
  <div class="cat-label" style="left:170px">HOME</div>
  <div class="cat" style="left:278px;background:linear-gradient(135deg,#eee,#b89a70)" role="img" aria-label="Seedling in an open hand for life insurance"></div>
  <div class="cat-label" style="left:295px">LIFE</div>
  <div class="cat" style="left:398px;background:linear-gradient(135deg,#ddd,#3f8a2a)" role="img" aria-label="Green medical cross for health insurance"></div>
  <div class="cat-label" style="left:406px">HEALTH</div>
  <div class="cat" style="left:518px;background:linear-gradient(135deg,#eee,#4a9a60)" role="img" aria-label="Nurse in green scrubs for long term care insurance"></div>
  <div class="cat-label" style="left:533px">CARE</div>
</section>
<aside class="abs register">
  <p>To Retrieve a quote, please Login above. or register with us to recieve instant quotes and updates.</p>
  <p class="cta">REGISTER &gt;&gt;</p>
</aside>

<aside class="abs sidebar">
  <div class="bar">NEWS &amp; INFORMATION</div>
  <div class="news">
    <div class="news-item">
      <div class="date">13 March 2010</div>
      <div>You could save upto 30% on your Car Insurance or home Insurance when you request a quote from Kvbrimtallow.com.</div>
      <div class="more">Want to know more?</div>
    </div>
    <div class="news-item">
      <div class="date">10 March 2010</div>
      <div>With stability in the economy, we could find insurance prices still remaining where they are</div>
      <div class="more">Want to know more?</div>
    </div>
  </div>
</aside>
<div class="abs side-btn" style="left:8px;top:684px">Need<br>Advise?</div>
<div class="abs side-btn" style="left:8px;top:753px">Make a<br>Claim?</div>

<section class="abs main" style="top:441px;height:169px">
  <div class="bar">WELCOME</div>
  <div class="copy">
    <p>Here at <b>Kvbrimtallow.com</b> we know the importance of insurance but equally know how important it is to make sure you don't end up over-paying for it. Comparing insurance with <b>Kvbrimtallow.com</b> has never been easier and helps you to find great deals available on the market today, all from the comfort of your own home, saving you both time and money at no extra cost.</p>
    <p>All you need to do is click to get a quote, fill in a few details about yourself and you could be comparing insurance prices from top providers in minutes. Whether you're looking for car insurance, home insurance, life insurance or insurance for long term care, you could save money with <b>Kvbrimtallow.com</b>.</p>
    <p>Find out how much you could save today and compare with <b>Kvbrimtallow.com</b></p>
  </div>
</section>

<section class="abs main help" style="top:615px;height:559px">
  <div class="bar">HERE TO HELP!</div>
  <div class="copy">Not sure what type of insurance you need, then simply complete this all-in-one form below and we'll see how we can save you money.</div>
</section>

<form>
  <div class="abs section-label" style="left:246px;top:724px">CONTACT INFO</div>
  <div class="abs form-label" style="left:200px;top:757px;width:101px">NAME:</div>
  <div class="abs field" style="left:307px;top:750px;width:181px"></div>
  <div class="abs form-label" style="left:480px;top:757px;width:131px">CONTACT NUMBER:</div>
  <div class="abs field" style="left:617px;top:750px;width:182px"></div>
  <div class="abs form-label" style="left:200px;top:791px;width:101px">EMAIL:</div>
  <div class="abs field" style="left:307px;top:784px;width:181px"></div>
  <div class="abs form-label" style="left:480px;top:792px;width:131px">BEST TIME TO CALL:</div>
  <div class="abs field" style="left:617px;top:785px;width:182px"></div>

  <div class="abs section-label" style="left:248px;top:825px">CAR INSURANCE</div>
  <div class="abs form-label" style="left:240px;top:865px;width:192px">ZIP WHERE CAR IS PAKED:</div>
  <div class="abs field" style="left:438px;top:858px;width:181px"></div>
  <div class="abs form-label" style="left:240px;top:896px;width:192px">YEAR:</div>
  <div class="abs field" style="left:438px;top:889px;width:181px"></div>
  <div class="abs form-label" style="left:240px;top:927px;width:192px">MAKE:</div>
  <div class="abs field" style="left:438px;top:920px;width:181px"></div>
  <div class="abs form-label" style="left:240px;top:958px;width:192px">MODEL:</div>
  <div class="abs field" style="left:438px;top:951px;width:181px"></div>
  <div class="abs form-label" style="left:240px;top:989px;width:192px">BODY TYPE:</div>
  <div class="abs field" style="left:438px;top:982px;width:181px"></div>
  <div class="abs form-label" style="left:240px;top:1019px;width:192px">No. OF DOORS:</div>
  <div class="abs field" style="left:438px;top:1012px;width:181px"></div>
  <div class="abs form-label" style="left:240px;top:1049px;width:192px">No. OF CYLINDERS:</div>
  <div class="abs field" style="left:438px;top:1042px;width:181px"></div>

  <div class="abs btn-caption" style="left:358px;top:1107px">Car Insurance Only Please.</div>
  <div class="abs btn-caption" style="left:547px;top:1107px">Next Page &gt; Home Insurance</div>
  <div class="abs pill" style="left:359px;top:1132px;width:141px;height:24px;font-weight:700;font-size:11px">SUBMIT</div>
  <div class="abs pill" style="left:557px;top:1132px;width:140px;height:24px;font-weight:700;font-size:11px">NEXT &gt;</div>
</form>

<footer class="abs footer">copyright © KVBRIMTALLOW.COM 2010</footer>

</body>
</html>
```